Business card design for Verdanta Building Systems
Verdanta Building Systems
Professional
Trevor Halloway
Director
418/37 Brindle St
Port Melbourne
VIC 3207
trevor@verdantabuilding.example.au
www.verdantabuilding.example.au
- Architectural Sunscreens
- Privacy Screens
- Modular/Continuous louvres
- Acoustic louvres
- Opening roof systems
- Handrail systems
- Custom Aluminium facades
- Architectural timber structures
this is the colours we like
front of card and back of card

```html
<!DOCTYPE html>
<html lang="en">
<head>
<meta charset="utf-8">
<title>Verdanta Building Systems – Business Card</title>
<link rel="stylesheet" href="https://fonts.googleapis.com/css2?family=Open+Sans:wght@400;600;700&display=swap">
<style>
  :root {
    --bg: #eceeec;
    --green: #2a9a55;
    --green-deep: #1c7440;
    --white: #ffffff;
    --paper: #f7f8f7;
    --rule: #d6d9d7;
    --ink-light: #e9f5ee;
    --ink-dark: #2c5f3f;
  }
  * { margin: 0; padding: 0; box-sizing: border-box; }
  html, body { width: 1200px; height: 629px; overflow: hidden; }
  body {
    background: var(--bg);
    font-family: "Open Sans", Arial, sans-serif;
    position: relative;
  }
  .card {
    position: absolute;
    top: 155px;
    width: 520px;
    height: 318px;
    border-radius: 4px;
    overflow: hidden;
    box-shadow: 0 6px 18px rgba(0,0,0,.16);
  }

  /* Back of card */
  .card-back {
    left: 50px;
    background: linear-gradient(160deg, var(--green) 0%, var(--green-deep) 100%);
  }
  .card-back .web {
    position: absolute;
    top: 20px; left: 22px;
    font-size: 8px;
    letter-spacing: .6px;
    color: var(--ink-light);
    opacity: .85;
  }
  .card-back .watermark-disc {
    position: absolute;
    left: 205px; top: 70px;
    width: 150px; height: 150px;
    border-radius: 50%;
    background: rgba(255,255,255,.07);
  }

  /* Front of card */
  .card-front {
    left: 630px;
    background: var(--white);
  }
  .front-top {
    position: absolute; inset: 0 0 auto 0;
    height: 166px;
    background: linear-gradient(180deg, var(--white) 0%, var(--paper) 100%);
    display: flex; align-items: center; justify-content: center; gap: 12px;
  }
  .brand-dot {
    width: 40px; height: 40px; border-radius: 50%;
    background: var(--green);
  }
  .brand-name {
    font-weight: 700;
    font-size: 19px;
    letter-spacing: 1.5px;
    color: var(--green-deep);
    text-transform: uppercase;
  }
  .front-rule {
    position: absolute; left: 0; right: 0; top: 166px;
    height: 8px; background: var(--rule);
  }
  .front-band {
    position: absolute; left: 0; right: 0; top: 174px; bottom: 0;
    background: linear-gradient(180deg, var(--green) 0%, var(--green-deep) 100%);
    color: var(--white);
  }
  .address {
    position: absolute; left: 16px; bottom: 14px;
    writing-mode: vertical-rl; transform: rotate(180deg);
    font-size: 7px; letter-spacing: .4px; color: var(--ink-light);
  }
  .person {
    position: absolute; right: 196px; top: 34px;
    text-align: right;
  }
  .person .name { font-size: 15px; font-weight: 700; }
  .person .title { font-size: 9px; margin-top: 3px; color: var(--ink-light); }
  .contacts {
    position: absolute; left: 338px; top: 28px;
    padding-left: 12px;
    border-left: 1px solid rgba(255,255,255,.6);
    list-style: none;
    font-size: 7.5px; line-height: 19px;
    color: var(--ink-light);
  }
  .contacts li { display: flex; align-items: center; gap: 6px; }
  .contacts svg { width: 9px; height: 9px; fill: none; stroke: var(--white); stroke-width: 1.4; }
</style>
</head>
<body>
  <section class="card card-back" aria-label="Back of card">
    <p class="web">www.verdantabuilding.example.au</p>
    <div class="watermark-disc"></div>
  </section>

  <section class="card card-front" aria-label="Front of card">
    <header class="front-top">
      <span class="brand-dot"></span>
      <span class="brand-name">Verdanta Building Systems</span>
    </header>
    <div class="front-rule"></div>
    <div class="front-band">
      <p class="address">418/37 Brindle St, Port Melbourne VIC 3207</p>
      <div class="person">
        <p class="name">Trevor Halloway</p>
        <p class="title">Director</p>
      </div>
      <ul class="contacts">
        <li><svg viewBox="0 0 10 10"><path d="M2 1h2l1 2.5-1.3 1a5 5 0 0 0 2 2l1-1.3L9 6v2a1 1 0 0 1-1 1A7 7 0 0 1 1 2a1 1 0 0 1 1-1z"/></svg>03 9000 1234</li>
        <li><svg viewBox="0 0 10 10"><rect x="2.5" y="1" width="5" height="8" rx="1"/></svg>0400 000 000</li>
        <li><svg viewBox="0 0 10 10"><rect x="1" y="2" width="8" height="6"/><path d="M1 2l4 3 4-3"/></svg>trevor@verdantabuilding.example.au</li>
        <li><svg viewBox="0 0 10 10"><circle cx="5" cy="5" r="4"/><path d="M1 5h8M5 1c2 2 2 6 0 8M5 1c-2 2-2 6 0 8"/></svg>www.verdantabuilding.example.au</li>
      </ul>
    </div>
  </section>
</body>
</html>
```